Unique Flyer Project - www.plumvaleforms.com.au

The purpose of this flyer is trying to get recipients to visit the website www.plumvaleforms.com.au and sign up to the offer. I need it to be simple/to the point, eye catching and professional. I will post up a basic idea I have but feel free to put your own spin on it if you think you have great ideas to get people to visit the site, if not then just improve upon the quality of mine and make it look like a respected company.

I also think a red band or something that REALLY catches the eye highlighting one of the important aspects of the flyer (the domain?) could be great so even if someone is about to put it in the bin, the popping red-on-white-background catches their eye so they end up looking at and reading the flyer.

I would also love a VERY SIMPLE design for the backside of the flyer, just a red box/band (whatever you think is good) with the domain 'www.plumvaleforms.com.au' in it. NOTHING ELSE! Just so if it's floating around the table and it's upside down, there's something eye catching that might entice the householder to look at it.

DESIGN IS FOR DL FLYER: 99mm X 210mm

Target Market(s)

Australian Residents interested in earning money from home.

Industry/Entity Type

It Company

Requirements
Must have
• Eye catching (mainly red band/box/bar on front & back page), SIMPLE, elegant/professional.
Should not have
• ANYTHING unnecessary to the reader that will distract them from the ultimate point - GET PAID TO DO SURVEYS FROM YOUR OWN HOME ON THE COMPUTER!

```html
<!DOCTYPE html>
<html lang="en">
<head>
<meta charset="utf-8">
<title>Plumvale Forms – DL Flyer</title>
<link rel="stylesheet" href="https://fonts.googleapis.com/css2?family=Nunito+Sans:ital,wght@0,400;0,700;0,800;0,900;1,400&display=swap">
<style>
  :root {
    --page-bg: #ececec;
    --card-edge: #8f8f8f;
    --sky-top: #ffffff;
    --sky-bottom: #49c1f7;
    --ink-blue: #1a1ee0;
    --logo-blue: #1f5fc4;
    --url-red: #e3131b;
    --pill-rim: #e4e6e8;
    --pill-line: #b9bdc1;
    --lens-light: #c9ecff;
    --lens-dark: #2a9be6;
    --badge-fill: #d8f1fb;
    --badge-line: #5fcdef;
    --flag-blue: #1a2d94;
    --white: #ffffff;
  }
  * { margin: 0; padding: 0; box-sizing: border-box; }
  html, body { width: 1155px; height: 1200px; overflow: hidden; }
  body {
    position: relative;
    background: var(--page-bg);
    font-family: "Nunito Sans", Arial, sans-serif;
  }
  .flyer-side {
    position: absolute;
    left: 95px;
    width: 964px;
    height: 453px;
    border: 1px solid var(--card-edge);
    overflow: hidden;
  }
  .flyer-front {
    top: 104px;
    background: linear-gradient(to bottom, var(--sky-top) 0%, #eaf8fe 40%, var(--sky-bottom) 100%);
  }
  .flyer-back { top: 640px; background: var(--white); }

  .brand {
    position: absolute;
    top: 52px;
    left: 0;
    width: 964px;
    display: flex;
    justify-content: center;
    align-items: center;
    gap: 12px;
    padding-right: 40px;
  }
  .brand-dot {
    width: 44px; height: 44px; border-radius: 50%;
    background: var(--logo-blue);
  }
  .brand-name {
    font-weight: 900;
    font-size: 46px;
    color: var(--logo-blue);
    letter-spacing: -0.5px;
  }

  .badge { position: absolute; left: 748px; top: 2px; width: 210px; height: 200px; }
  .badge-text {
    position: absolute;
    left: 808px; top: 126px;
    width: 86px;
    font-size: 10px; font-weight: 800; line-height: 1.15;
    text-align: center; color: #222;
    transform: rotate(8deg);
  }

  .tagline, .headline, .subline {
    position: absolute; left: 0; width: 964px; text-align: center; padding-right: 40px;
  }
  .tagline { top: 160px; font-style: italic; font-size: 31px; color: var(--ink-blue); }
  .headline { top: 206px; font-weight: 700; font-size: 49px; color: var(--ink-blue); letter-spacing: 0.3px; }
  .subline { top: 285px; font-size: 25px; color: var(--white); }

  .search-pill { position: absolute; }
  .search-pill svg { position: absolute; left: 0; top: 0; }
  .search-url {
    position: absolute; color: var(--url-red); white-space: nowrap;
  }
  .search-pill.front { left: 190px; top: 330px; width: 566px; height: 96px; }
  .search-pill.front .search-url { left: 25px; top: 26px; font-size: 30px; }
  .search-pill.back { left: 120px; top: 156px; width: 743px; height: 124px; }
  .search-pill.back .search-url { left: 33px; top: 34px; font-size: 40px; }
</style>
</head>
<body>

<section class="flyer-side flyer-front">
  <div class="brand">
    <span class="brand-dot"></span>
    <span class="brand-name">Plumvale Forms</span>
  </div>

  <svg class="badge" viewBox="0 0 210 200" aria-hidden="true">
    <path fill="var(--badge-fill)" stroke="var(--badge-line)" stroke-width="3"
      d="M105 6 Q120 20 138 12 Q146 30 166 30 Q166 50 184 60 Q174 76 188 94 Q172 106 178 126 Q158 130 152 150 Q134 146 122 162 Q108 150 90 160 Q80 142 60 144 Q58 124 38 118 Q46 100 32 86 Q48 74 42 54 Q62 52 70 32 Q88 38 105 6 Z"
      transform="translate(4 18) scale(1)"/>
  </svg>
  <svg role="img" aria-label="Australian flag" style="position:absolute;left:792px;top:54px" width="128" height="74" viewBox="0 0 128 74">
    <rect x="2" y="2" width="122" height="64" fill="var(--flag-blue)" transform="rotate(4 64 34)"/>
  </svg>
  <div class="badge-text">NOW OPEN TO RESIDENTS OF AUSTRALIA</div>

  <p class="tagline">Could you use an extra income?</p>
  <p class="headline">Earn as much as $50 per survey!</p>
  <p class="subline">Work from home and choose your own hours!</p>

  <div class="search-pill front">
    <svg width="566" height="96" viewBox="0 0 566 96" aria-hidden="true">
      <defs>
        <radialGradient id="lensA" cx="40%" cy="30%" r="75%">
          <stop offset="0" stop-color="var(--lens-light)"/>
          <stop offset="1" stop-color="var(--lens-dark)"/>
        </radialGradient>
      </defs>
      <rect x="1" y="1" width="564" height="94" rx="47" fill="var(--pill-rim)" stroke="#d0d3d6"/>
      <rect x="12" y="12" width="540" height="72" rx="36" fill="var(--white)" stroke="var(--pill-line)" stroke-width="1.5"/>
      <circle cx="520" cy="48" r="35" fill="url(#lensA)" stroke="#1d86d4" stroke-width="2"/>
      <circle cx="514" cy="42" r="12" fill="none" stroke="var(--white)" stroke-width="4"/>
      <line x1="523" y1="51" x2="536" y2="64" stroke="var(--white)" stroke-width="6" stroke-linecap="round"/>
    </svg>
    <span class="search-url">www.plumvaleforms.com.au</span>
  </div>
</section>

<section class="flyer-side flyer-back">
  <div class="search-pill back">
    <svg width="743" height="124" viewBox="0 0 743 124" aria-hidden="true">
      <defs>
        <radialGradient id="lensB" cx="40%" cy="30%" r="75%">
          <stop offset="0" stop-color="var(--lens-light)"/>
          <stop offset="1" stop-color="var(--lens-dark)"/>
        </radialGradient>
      </defs>
      <rect x="1" y="1" width="741" height="122" rx="61" fill="var(--pill-rim)" stroke="#d0d3d6"/>
      <rect x="15" y="15" width="710" height="94" rx="47" fill="var(--white)" stroke="var(--pill-line)" stroke-width="1.5"/>
      <circle cx="680" cy="62" r="45" fill="url(#lensB)" stroke="#1d86d4" stroke-width="2"/>
      <circle cx="673" cy="54" r="15" fill="none" stroke="var(--white)" stroke-width="5"/>
      <line x1="684" y1="66" x2="700" y2="82" stroke="var(--white)" stroke-width="7" stroke-linecap="round"/>
    </svg>
    <span class="search-url">www.plumvaleforms.com.au</span>
  </div>
</section>

</body>
</html>
```